Realtor Business Card for Marisol!

I sell real estate in a tropical location near the ocean, beaches and palm trees.

The homes are higher end, luxury. I want a card that is professional and attention-grabbing. In a sea full of competition, I need to stand out! I don't want the run-of-the mill card that looks like everyone else's with a different name. I want people to say "wow!".
Updates

Project Deadline Extended Reason: I have a little more time that originally anticipated. Added Friday, July 7, 2017

Target Market(s)

All.

Industry/Entity Type

Real Estate Agent

Contact Information for Business Card

Name: Marisol Vankeer-Odham
Email: marisol@harborview-estates.example
Website: www.harborviewestates.example
Phone: 555.418.7263

Font styles to use
Serif

Colors

Designer to choose colors to be used in the design.

Requirements
Must have
• All attachments.
Nice to have
• Gold edges
• Transparent card
• Unique shape

```html
<!DOCTYPE html>
<html lang="en">
<head>
<meta charset="utf-8">
<title>Harborview Estates – Business Card</title>
<link rel="stylesheet" href="https://fonts.googleapis.com/css2?family=Open+Sans:ital,wght@0,300;0,400;0,700;1,300&display=swap">
<style>
  :root {
    --paper: #ffffff;
    --ink: #2b2b2b;
    --ink-strong: #1a1a1a;
    --gold-bright: #f5e400;
    --gold-deep: #8a5a12;
    --photo-light: #c4c4c4;
    --photo-mid: #7d7d7d;
    --photo-dark: #4e4e4e;
    --card-shadow: rgba(0, 0, 0, 0.18);
  }
  html, body {
    margin: 0;
    width: 1200px;
    height: 1200px;
    overflow: hidden;
    background: var(--paper);
    font-family: "Open Sans", sans-serif;
  }
  .canvas {
    position: relative;
    width: 1200px;
    height: 1200px;
  }
  .card {
    position: absolute;
    left: 152px;
    width: 874px;
    background: var(--paper);
    box-shadow: 0 6px 16px var(--card-shadow);
  }
  .card svg { display: block; width: 100%; height: 100%; overflow: visible; }
  .card--front { top: 186px; height: 444px; }
  .card--back  { top: 682px; height: 446px; }

  .wordmark-small { font-weight: 300; font-size: 40px; fill: var(--ink); letter-spacing: 1px; }
  .wordmark-large { font-weight: 300; font-size: 88px; fill: var(--ink); }
  .brand-name   { font-weight: 700; font-size: 31px; fill: var(--ink-strong); letter-spacing: 1px; }
  .brand-sub    { font-weight: 700; font-size: 26px; fill: var(--ink-strong); letter-spacing: 1px; }
  .contact-line { font-weight: 300; font-size: 20px; fill: var(--ink); }
  .contact-web  { font-weight: 300; font-style: italic; font-size: 17px; fill: var(--ink); }
  .rule         { stroke: var(--ink-strong); stroke-width: 3; }
  .frame-gold   { fill: none; stroke: url(#goldFade); stroke-width: 3; }
  .frame-yellow { fill: none; stroke: var(--gold-bright); stroke-width: 3; }
</style>
</head>
<body>
<main class="canvas">

  <section class="card card--front" aria-label="Card front">
    <svg viewBox="0 0 728 370" xmlns="http://www.w3.org/2000/svg">
      <defs>
        <linearGradient id="coastTone" x1="0" y1="0" x2="0" y2="1">
          <stop offset="0" stop-color="var(--photo-mid)"/>
          <stop offset="0.45" stop-color="var(--photo-dark)"/>
          <stop offset="0.65" stop-color="var(--photo-light)"/>
          <stop offset="1" stop-color="var(--photo-mid)"/>
        </linearGradient>
        <linearGradient id="goldFade" x1="0" y1="0" x2="0" y2="1">
          <stop offset="0" stop-color="var(--gold-deep)"/>
          <stop offset="0.5" stop-color="var(--gold-bright)"/>
          <stop offset="1" stop-color="var(--gold-bright)"/>
        </linearGradient>
      </defs>

      <text class="wordmark-small" x="490" y="45" text-anchor="end">ESTATES</text>
      <text class="wordmark-large" x="33" y="117" textLength="457" lengthAdjust="spacingAndGlyphs">HARBORVIEW</text>

      <path class="coast-photo" role="img" aria-label="Black and white photo of a beachfront with villas and palm trees"
            d="M0,215 C40,150 90,138 140,152 C230,180 300,222 380,212 C460,200 500,120 600,117 L728,117 L728,370 L0,370 Z"
            fill="url(#coastTone)"/>

      <path class="frame-gold" d="M542,0 L542,197 L649,197 L649,0"/>
      <path class="frame-yellow" d="M728,100 L530,100 L530,207 L728,207"/>
    </svg>
  </section>

  <section class="card card--back" aria-label="Card back">
    <svg viewBox="0 0 728 372" xmlns="http://www.w3.org/2000/svg">
      <defs>
        <linearGradient id="portraitTone" x1="0" y1="0" x2="0" y2="1">
          <stop offset="0" stop-color="var(--photo-light)"/>
          <stop offset="0.5" stop-color="var(--photo-mid)"/>
          <stop offset="1" stop-color="var(--photo-dark)"/>
        </linearGradient>
      </defs>

      <rect class="agent-portrait" role="img" aria-label="Black and white portrait of the agent"
            x="36" y="54" width="92" height="144" fill="url(#portraitTone)"/>
      <path class="frame-yellow" d="M34,0 L34,202 L130,202 L130,0"/>

      <text class="brand-name" x="366" y="212" text-anchor="middle">HARBORVIEW</text>
      <text class="brand-sub" x="366" y="240" text-anchor="middle">ESTATES</text>

      <text class="contact-line" x="683" y="257" text-anchor="end">(555)418-7263</text>
      <text class="contact-line" x="683" y="282" text-anchor="end">Marisol Vankeer-Odham</text>

      <line class="rule" x1="48" y1="296" x2="691" y2="296"/>
      <line class="rule" x1="379" y1="296" x2="379" y2="331"/>

      <text class="contact-web" x="48" y="330">marisol@harborview-estates.example</text>
      <text class="contact-web" x="681" y="330" text-anchor="end">www.harborviewestates.example</text>
    </svg>
  </section>

</main>
</body>
</html>
```